Business Card Design

we are Koorawatha Orchards & we would like a business card that stands out from the crowd and that we can apply this design to our products as we will be also placing orders for labels and stickers in the future

Industry/Entity Type

Business

Contact Information for Business Card

Packing Shed : 54 917 360
mobile : 0428 351 904
email : koorawathaorchards@fernmail.net.au
address : Pelican Crescent Tarrawong 4578

```html
<!DOCTYPE html>
<html lang="en">
<head>
<meta charset="utf-8">
<title>Koorawatha Orchards – Business Card</title>
<link href="https://fonts.googleapis.com/css2?family=Arvo:wght@400&family=Roboto:wght@400&display=swap" rel="stylesheet">
<style>
  :root {
    --page: #e8e5e0;
    --card: #ffffff;
    --card-shade: #eeeeee;
    --leaf-green: #1f6b3a;
    --line-green: #17602f;
    --berry-red: #d7262e;
    --berry-deep: #8e0f16;
    --berry-light: #e8434a;
  }
  * { margin: 0; padding: 0; box-sizing: border-box; }
  html, body {
    width: 1200px; height: 780px; overflow: hidden;
    background: var(--page);
  }
  .canvas {
    position: relative; width: 1200px; height: 780px;
    display: flex; flex-direction: column; align-items: center; justify-content: center;
    gap: 28px;
  }
  .card {
    position: relative; width: 620px; height: 354px;
    background: linear-gradient(135deg, var(--card) 40%, var(--card-shade));
    border-radius: 14px; overflow: hidden;
    box-shadow: 0 4px 14px rgba(0,0,0,.14);
  }
  .card-art { position: absolute; inset: 0; width: 100%; height: 100%; }
  .brand {
    position: absolute; left: 0; right: 0;
    display: flex; flex-direction: column; align-items: center;
    font-family: "Arvo", Georgia, serif; font-weight: 400;
    color: var(--leaf-green); text-transform: uppercase; line-height: 1;
    white-space: nowrap;
  }
  .brand-name-top { font-size: 28px; letter-spacing: 2px; }
  .brand-mark {
    width: 34px; height: 34px; border-radius: 50%;
    background: var(--berry-red); margin: 9px 0;
  }
  .brand-name-bottom { font-size: 21px; letter-spacing: 2px; }
  .card-front .brand { top: 38px; }
  .card-back .brand { top: 86px; }
  .card-back .brand-name-top { font-size: 32px; }
  .card-back .brand-name-bottom { font-size: 25px; }
  .card-back .brand-mark { width: 44px; height: 44px; margin: 13px 0; }
  .contact {
    position: absolute; left: 0; right: 0; top: 196px;
    list-style: none; text-align: center; white-space: nowrap;
    font-family: "Roboto", Arial, sans-serif; font-size: 11px; line-height: 19px;
    color: var(--leaf-green);
  }
  .contact .label { color: var(--berry-red); }
</style>
</head>
<body>
<main class="canvas">

  <section class="card card-front">
    <svg class="card-art" viewBox="0 0 620 354">
      <defs>
        <linearGradient id="berryFront" x1="0" y1="0" x2="1" y2="1">
          <stop offset="0" stop-color="#e8434a"/>
          <stop offset="0.6" stop-color="#d7262e"/>
          <stop offset="1" stop-color="#8e0f16"/>
        </linearGradient>
      </defs>
      <path role="img" aria-label="Close-up photograph of a ripe strawberry" d="M0 60 H120 Q70 177 120 294 H0 Z" fill="url(#berryFront)"/>
      <path role="img" aria-label="Close-up photograph of a ripe strawberry with green leaves" d="M620 60 H500 Q550 177 500 294 H620 Z" fill="url(#berryFront)"/>
      <g stroke="#17602f" stroke-width="2">
        <line x1="0" y1="51" x2="120" y2="51"/><line x1="0" y1="56" x2="120" y2="56"/>
        <line x1="0" y1="298" x2="120" y2="298"/><line x1="0" y1="303" x2="120" y2="303"/>
        <line x1="500" y1="51" x2="620" y2="51"/><line x1="500" y1="56" x2="620" y2="56"/>
        <line x1="500" y1="298" x2="620" y2="298"/><line x1="500" y1="303" x2="620" y2="303"/>
      </g>
    </svg>
    <div class="brand">
      <span class="brand-name-top">Koorawatha</span>
      <span class="brand-mark"></span>
      <span class="brand-name-bottom">Orchards</span>
    </div>
    <ul class="contact">
      <li><span class="label">Packing Shed:</span> 54 917 360</li>
      <li><span class="label">mobile:</span> 0428 351 904 | <span class="label">email:</span> koorawathaorchards@fernmail.net.au</li>
      <li><span class="label">address:</span> Pelican Crescent Tarrawong 4578</li>
    </ul>
  </section>

  <section class="card card-back">
    <svg class="card-art" viewBox="0 0 620 354">
      <defs>
        <linearGradient id="berryBack" x1="0" y1="0" x2="1" y2="1">
          <stop offset="0" stop-color="#e8434a"/>
          <stop offset="0.6" stop-color="#d7262e"/>
          <stop offset="1" stop-color="#8e0f16"/>
        </linearGradient>
      </defs>
      <path role="img" aria-label="Close-up photograph of a ripe strawberry" d="M0 60 H120 Q70 177 120 294 H0 Z" fill="url(#berryBack)"/>
      <path role="img" aria-label="Close-up photograph of a ripe strawberry with green leaves" d="M620 60 H500 Q550 177 500 294 H620 Z" fill="url(#berryBack)"/>
      <g stroke="#17602f" stroke-width="2">
        <line x1="0" y1="51" x2="120" y2="51"/><line x1="0" y1="56" x2="120" y2="56"/>
        <line x1="0" y1="298" x2="120" y2="298"/><line x1="0" y1="303" x2="120" y2="303"/>
        <line x1="500" y1="51" x2="620" y2="51"/><line x1="500" y1="56" x2="620" y2="56"/>
        <line x1="500" y1="298" x2="620" y2="298"/><line x1="500" y1="303" x2="620" y2="303"/>
      </g>
    </svg>
    <div class="brand">
      <span class="brand-name-top">Koorawatha</span>
      <span class="brand-mark"></span>
      <span class="brand-name-bottom">Orchards</span>
    </div>
  </section>

</main>
</body>
</html>
```